Wren Sporting Goods Inc.

Need to create a website that is informational and has the ability to sell goods and services. Such as a custom t shirt designer where the user can upload and image to be displayed on the garmet. The sports we specialize in are basketball, football, and baseball.

Would like like:
Home Page
Locker Room Page:
Custom Uniforms Page
Custom Shirt Creator
Brands
About

Competitor websites are
tundrafieldwearnx.com
dvq.com
lumarogear.com

```html
<!DOCTYPE html>
<html lang="en">
<head>
<meta charset="utf-8">
<title>Wren Sporting Goods – Design Your Own</title>
<link href="https://fonts.googleapis.com/css2?family=Archivo+Black&family=Sora:wght@400;500;600;700&family=Inter:wght@400;500;600&display=swap" rel="stylesheet">
<style>
:root{
  --ink:#1b1b1f;
  --muted:#4a4a52;
  --blue:#1f63c9;
  --red:#d33a35;
  --soft:#f1f2f4;
  --circle:#eef3fb;
  --line:#d9d9de;
  --white:#ffffff;
}
*{margin:0;padding:0;box-sizing:border-box}
html,body{width:1200px;height:3729px;overflow:hidden}
body{position:relative;background:var(--white);color:var(--ink);font-family:"Inter",sans-serif}
.abs{position:absolute}
.photo{position:absolute;border-radius:6px;overflow:hidden}
.arrow{width:14px;height:14px;vertical-align:-2px;margin-left:10px}

/* hero */
.hero{left:0;top:0;width:1200px;height:709px;background:linear-gradient(135deg,#3b3f45 0%,#5a4a4a 35%,#2e3a2f 70%,#4b2d2d 100%)}
.hero::after{content:"";position:absolute;inset:0;background:linear-gradient(90deg,rgba(10,12,16,.55),rgba(10,12,16,.15))}
.nav{left:78px;top:22px;width:1042px;height:50px;border:1px solid rgba(255,255,255,.45);background:rgba(255,255,255,.1);z-index:2}
.brand{position:absolute;left:20px;top:10px;display:flex;align-items:center;gap:8px;font-family:"Sora",sans-serif;font-weight:700;font-size:15px;color:var(--white)}
.brand .dot{width:14px;height:14px;border-radius:50%;background:var(--red)}
.menu{position:absolute;left:364px;top:17px;display:flex;gap:14px;font-size:12px;color:#f0f0f0}
.pill{position:absolute;height:34px;border-radius:17px;color:var(--white);font-weight:500;font-size:14px;display:flex;align-items:center;justify-content:center}
.hero-title{left:78px;top:232px;font-family:"Archivo Black",sans-serif;font-size:72px;line-height:80px;letter-spacing:-3px;color:var(--white);z-index:2}
.hero-title span{color:var(--red);display:block}
.hero-copy{left:79px;top:410px;width:680px;font-size:19.5px;line-height:30px;color:#f1f1f1;z-index:2}
.btn{position:absolute;height:40px;border-radius:20px;font-size:16px;font-weight:500;display:flex;align-items:center;justify-content:center;z-index:2}

/* how it works */
.section-title{font-family:"Sora",sans-serif;font-weight:600;font-size:37px;letter-spacing:-.5px}
.step{position:absolute;width:320px;text-align:center}
.step .num{width:72px;height:72px;margin:0 auto;border-radius:50%;background:var(--circle);color:var(--red);font-family:"Sora",sans-serif;font-size:30px;font-weight:500;display:flex;align-items:center;justify-content:center}
.step h3{margin-top:16px;font-family:"Sora",sans-serif;font-weight:500;font-size:24px}
.step p{margin-top:12px;font-size:13.5px;line-height:20px;color:var(--muted)}

/* gear */
.gear{left:0;top:1064px;width:1200px;height:685px;background:var(--soft)}
.card-label{position:absolute;left:14px;bottom:38px;font-family:"Sora",sans-serif;font-weight:700;font-size:25px;color:var(--white)}
.tag{position:absolute;left:14px;bottom:32px;height:34px;padding:0 20px;border-radius:17px;background:var(--white);font-family:"Sora",sans-serif;font-size:18px;display:flex;align-items:center}

/* team banner */
.team{left:0;top:2839px;width:1200px;height:253px;background:linear-gradient(100deg,#3a2a32 0%,#6b3440 45%,#3c2a3a 75%,#5a2f3a 100%)}
.team::after{content:"";position:absolute;inset:0;background:rgba(20,16,30,.45)}

/* newsletter & footer */
.input{left:787px;top:3161px;width:222px;height:41px;border:1px solid #8a8a90;font-size:12px;color:#777;padding:13px 10px}
.subscribe{left:1022px;top:3161px;width:100px;height:41px;border:1px solid #8a8a90;font-size:13px;display:flex;align-items:center;justify-content:center}
.rule{left:78px;width:1044px;height:1px;background:var(--line)}
.foot-col{position:absolute;font-size:12px;color:#333}
.foot-col h4{font-size:12.5px;font-weight:600;color:var(--ink);margin-bottom:14px}
.post .date{font-size:17px;color:#777}
.post .date small{font-size:10px;margin-left:6px}
.post p{font-size:13px;line-height:18px;color:#333;margin-top:8px}
.post .c{font-size:10.5px;color:#888;margin-top:8px}
.social{position:absolute;top:3674px;width:14px;height:14px;border-radius:50%;background:#222}
</style>
</head>
<body>

<!-- Hero -->
<div class="abs hero" role="img" aria-label="Photo of American football players in red and navy jerseys running on the field"></div>
<nav class="abs nav">
  <div class="brand"><span class="dot"></span>Wren Sporting Goods</div>
  <div class="menu"><span>Locker Room</span><span>Custom Uniforms</span><span>Custom Shirt Creator</span><span>Brands</span><span>About</span></div>
  <div class="pill" style="left:798px;top:7px;width:137px;background:var(--blue)">Srart Designing</div>
  <div class="pill" style="left:955px;top:7px;width:68px;background:var(--red)">Shop</div>
</nav>
<h1 class="abs hero-title">Design Your Own.<span>Wear Your Pride.</span></h1>
<p class="abs hero-copy">From chip architecture to high-performance silicon, we deliver cutting-edge IP development and engineering services that power the world's most advanced technologies.</p>
<a class="btn" style="left:78px;top:533px;width:252px;background:var(--blue);color:var(--white)">Launch Custom Creator<svg class="arrow" viewBox="0 0 14 14" fill="none" stroke="currentColor" stroke-width="1.8"><path d="M3 11L11 3M5 3h6v6"/></svg></a>
<a class="btn" style="left:365px;top:533px;width:246px;border:1px solid rgba(255,255,255,.6);background:rgba(0,0,0,.25);color:var(--white)">Explore Team Uniforms<svg class="arrow" viewBox="0 0 14 14" fill="none" stroke="currentColor" stroke-width="1.8"><path d="M3 11L11 3M5 3h6v6"/></svg></a>

<!-- How it works -->
<h2 class="abs section-title" style="left:0;width:1200px;top:750px;text-align:center">How It Works</h2>
<div class="step" style="left:61px;top:843px"><div class="num">1</div><h3>Upload &amp; Design</h3><p>Upload your logo or use our templates. Our<br>online designer makes it easy.</p></div>
<div class="step" style="left:442px;top:843px"><div class="num">2</div><h3>Choose Your Gear</h3><p>Select from 500+ official jerseys, performance<br>tees, and hoodies from top brands.</p></div>
<div class="step" style="left:823px;top:843px"><div class="num">3</div><h3>Ship &amp; Represent</h3><p>Approve your free digital proof. We print,<br>embroider, and ship directly to you.</p></div>

<!-- Gear for your game -->
<section class="abs gear"></section>
<h2 class="abs section-title" style="left:84px;top:1154px">Gear For Your Game</h2>
<a class="abs" style="right:78px;top:1166px;font-family:'Sora',sans-serif;font-size:19px;color:var(--blue)">View All Sports</a>
<div class="photo" style="left:78px;top:1226px;width:335px;height:456px;background:linear-gradient(180deg,#5a3a36,#7a4a44 50%,#3a2a2a)" role="img" aria-label="Photo of a basketball player dunking"><span class="card-label">Basketball</span></div>
<div class="photo" style="left:433px;top:1226px;width:334px;height:456px;background:linear-gradient(180deg,#1c2430,#2a3a5a 45%,#4a4a3a)" role="img" aria-label="Photo of a soccer player in blue leaping for the ball at night"><span class="card-label">Football</span></div>
<div class="photo" style="left:787px;top:1226px;width:335px;height:456px;background:linear-gradient(180deg,#3f5a4a,#8a5a50 55%,#6a4a3a)" role="img" aria-label="Photo of a baseball batter in a red jersey at the plate"><span class="card-label">Baseball</span></div>

<!-- Worn by champions -->
<h2 class="abs section-title" style="left:0;width:1230px;top:1794px;text-align:center">Worn By Champions</h2>
<p class="abs" style="left:0;width:1230px;top:1844px;text-align:center;font-size:18px;color:#333">Real Teams, Real Games, Real Gear Get Inspired By The Community</p>
<div class="photo" style="left:78px;top:1912px;width:335px;height:375px;background:linear-gradient(160deg,#3a3430,#6a5a4a 50%,#4a3a30)" role="img" aria-label="Photo of a basketball game under the hoop"><span class="tag">Basketball</span></div>
<div class="photo" style="left:433px;top:1912px;width:334px;height:375px;background:linear-gradient(160deg,#3a5a30,#5a7a3a 50%,#3a5a2a)" role="img" aria-label="Photo of two soccer players jumping for the ball"><span class="tag">Football</span></div>
<div class="photo" style="left:787px;top:1912px;width:335px;height:375px;background:linear-gradient(160deg,#1a1a1c,#3a3a3c 55%,#5a4a3a)" role="img" aria-label="Photo of a baseball batter and catcher at night"><span class="tag">Baseball</span></div>
<div class="photo" style="left:78px;top:2309px;width:335px;height:373px;background:linear-gradient(160deg,#b85a52,#c86a60 50%,#a04a44)" role="img" aria-label="Aerial photo of runners on a red track"><span class="tag">Track &amp; Field</span></div>
<div class="photo" style="left:433px;top:2309px;width:334px;height:373px;background:linear-gradient(160deg,#4a5a4a,#8a8a88 50%,#5a3a3a)" role="img" aria-label="Photo of football players in white and red game jerseys"><span class="tag">Game Jerseys</span></div>
<div class="photo" style="left:787px;top:2309px;width:335px;height:373px;background:linear-gradient(160deg,#5a5a60,#7a2a30 55%,#3a1a20)" role="img" aria-label="Photo of a team in red jerseys celebrating"><span class="tag">See More</span></div>
<a class="btn" style="left:460px;top:2724px;width:278px;height:41px;background:var(--soft);color:var(--ink);font-size:15px">View Gallery &amp; Get Inspired<svg class="arrow" viewBox="0 0 14 14" fill="none" stroke="currentColor" stroke-width="1.8"><path d="M3 11L11 3M5 3h6v6"/></svg></a>

<!-- Team banner -->
<section class="abs team" role="img" aria-label="Photo of a baseball player in a red cap with a crowd behind"></section>
<h2 class="abs" style="left:104px;top:2900px;font-family:'Sora',sans-serif;font-weight:600;font-size:42px;color:var(--white);z-index:2">Ordering For A Team Or League?</h2>
<p class="abs" style="left:104px;top:2962px;width:700px;font-size:19.5px;line-height:30px;color:#eee;z-index:2">Professional Jerseys &amp; Fanwear for Basketball, Football, and Baseball. From Concept to Field in Weeks.</p>
<a class="btn" style="left:874px;top:2947px;width:222px;height:36px;border-radius:6px;background:var(--blue);color:var(--white)">Contact Team Sales<svg class="arrow" viewBox="0 0 14 14" fill="none" stroke="currentColor" stroke-width="1.8"><path d="M3 11L11 3M5 3h6v6"/></svg></a>

<!-- Newsletter -->
<h2 class="abs" style="left:78px;top:3166px;font-family:'Inter',sans-serif;font-weight:500;font-size:26px">Join our newsletter</h2>
<p class="abs" style="left:78px;top:3204px;font-size:13px">Lorem ipsum dolor sit amet, consectetur adipiscing elit.</p>
<div class="abs input">Enter your email</div>
<div class="abs subscribe">Subscribe</div>
<p class="abs" style="left:787px;top:3214px;font-size:9px">By subscribing you agree to with our <u>Privacy Policy</u></p>
<div class="abs rule" style="top:3274px"></div>

<!-- Footer -->
<div class="foot-col" style="left:78px;top:3324px">
  <h4>Quick Link</h4>
  <div style="line-height:28.5px">Locker Room<br>Custom Uniforms<br>Custom Shirt Creator<br>Brands<br>About</div>
</div>
<div class="foot-col" style="left:347px;top:3324px">
  <h4>Support</h4>
  <div style="line-height:31px;margin-top:6px">Contact Us<br>Terms and Condition<br>Privacy Policy<br>Talk Us</div>
</div>
<div class="foot-col" style="left:617px;top:3324px">
  <h4>Latest Blog And Articles</h4>
  <div style="line-height:31px;margin-top:6px">Blog no 1<br>Blog no 1<br>Blog no 1<br>Blog no 1<br>Blog no 1</div>
</div>
<div class="foot-col" style="left:886px;top:3324px;width:236px">
  <h4>Column Five</h4>
  <div class="post" style="margin-top:12px"><div class="date">26<small>May</small></div><p>Lorem ipsum dolor sit amet,<br>consectetur adipiscing elit.</p><div class="c">3 comments</div></div>
  <div style="height:1px;background:#999;margin:22px 0 26px"></div>
  <div class="post"><div class="date">27<small>May</small></div><p>Lorem ipsum dolor sit amet,<br>consectetur adipiscing elit.</p><div class="c">3 comments</div></div>
</div>
<div class="abs rule" style="top:3639px"></div>
<div class="abs" style="left:84px;top:3674px;display:flex;align-items:center;gap:8px;font-family:'Sora',sans-serif;font-weight:700;font-size:15px;color:var(--blue)"><span style="width:14px;height:14px;border-radius:50%;background:var(--red)"></span>Wren Sporting Goods</div>
<span class="social" style="left:528px" aria-label="Social profile"></span>
<span class="social" style="left:567px" aria-label="Social profile"></span>
<span class="social" style="left:610px" aria-label="Social profile"></span>
<span class="social" style="left:653px" aria-label="Social profile"></span>
<p class="abs" style="right:88px;top:3677px;font-size:11px;color:#333">© 2025 Wren Sporting Goods. All rights reserved.</p>

</body>
</html>
```